Corvane Plant Trading Company - Enhance our webpage

We have an existing website - please see www.brackwoodtooling.com. The text in there is fundamentally what we want to say. There is also a search function where you can search our database, which is crucial to the site. We are happy with our logo, top left-hand side and want it to remain as it is. Everything else, including pictures, drawings and animation can be changed. In general, the website looks a little tired and the icons on the tabs need creative input.

We want our website to look dynamic, eye-catching, bold, very professional, modern and also uphold our impeccable 30-year reputation in the business.

We are essentially looking for a young, dynamic mind to provide our website with some inspiration. We encourage all designers to use their imagination and surprise us.

We have technical people to do the technical work, such as coding, but what we are looking for is asthetic creativity.

In addition, we have seen our competitors offer a translation service on their website i.e. you can just click on a flag and the website will turn into a different language. If you can incorporate this, it would be very useful.
Updates

Reason: Hi All - we have received some fantastic designs, so thank you. We are extending the deadline so that people can upgrade theirs slightly. We haven't seen enough dynamism with pictures and icons. And for those who have shown dynamism in those departments, we would also like you to consider including a video on the home page of some sort. You can find many videos of working machines like these on Clip-Vista. Thanks.

Target Market(s)

International Engineering companies

Industry/Entity Type

Flag

Requirements
Must have
• The "search database" facility must remain there.
Nice to have
• Perhaps some working videos running on the homepage of some of the types of machines we sell. You can find many such videos on ClipVista. We will constantly change those as we get new stock in.

```html
<!DOCTYPE html>
<html lang="en">
<head>
<meta charset="utf-8">
<title>Brackwood Tooling – World-class CNC Conventional Machine Tools</title>
<link rel="stylesheet" href="https://fonts.googleapis.com/css2?family=Noto+Serif:wght@400;700&family=Open+Sans:wght@400;600;700&display=swap">
<style>
  :root{
    --page:#4a4a4a;
    --topbar:#0b0b0b;
    --header-top:#3a3a3a;
    --header-bottom:#1c1c1c;
    --green:#7aab12;
    --green-dark:#5d8a0a;
    --red:#d9221c;
    --promo:#ff3514;
    --white:#ffffff;
    --ink:#1a1a1a;
    --muted:#8c8c8c;
    --footer:#2b2b2b;
    --footer-line:#8a5a66;
    --serif:"Noto Serif", Georgia, serif;
    --sans:"Open Sans", Arial, sans-serif;
  }
  *{box-sizing:border-box;margin:0;padding:0}
  html,body{width:1200px;height:2238px;overflow:hidden}
  body{position:relative;background:var(--page);font-family:var(--serif);color:var(--white)}
  .abs{position:absolute}

  /* top bar */
  .topbar{left:0;top:0;width:1200px;height:43px;background:var(--topbar);font-size:12px;font-family:var(--serif)}
  .topbar .links{left:59px;top:14px;display:flex;gap:16px;color:#aaa}
  .topbar .links span:first-child{color:#fff}
  .topbar .register{left:467px;top:14px;color:#8a8a8a}
  .topbar .register .signup{color:#7aab12}
  .topbar .register .login{color:#fff}
  .topbar .call{left:992px;top:14px;color:#fff}

  /* header */
  .header{left:0;top:43px;width:1200px;height:88px;background:linear-gradient(var(--header-top),var(--header-bottom));border-bottom:1px solid #555}
  .brand{left:50px;top:18px;display:flex;align-items:center;gap:12px}
  .brand-mark{width:22px;height:22px;background:var(--white)}
  .brand-name{font-family:var(--serif);font-weight:700;font-size:34px;color:var(--white);letter-spacing:1px}
  .nav{left:460px;top:0;height:88px;display:flex}
  .nav a{display:flex;align-items:center;justify-content:center;height:88px;border-left:2px solid #0e0e0e;box-shadow:inset 1px 0 0 #555;color:#eee;text-decoration:none;font-size:18px}
  .nav a:nth-child(1){width:95px}
  .nav a:nth-child(2){width:192px}
  .nav a:nth-child(3){width:160px}
  .nav a:nth-child(4){width:155px}
  .nav a:nth-child(5){width:90px}

  /* slider */
  .slider{left:54px;top:152px;width:1093px;height:627px;background:#2a2a2a}
  .slider-photo{left:0;top:0;width:1093px;height:571px;background:radial-gradient(ellipse at 45% 55%,#b8641c 0%,#6e3a12 35%,#2a1a10 70%,#140e0b 100%)}
  .slider-overlay{left:0;top:0}
  .slider-copy{right:22px;top:10px;text-align:right;width:460px}
  .slider-copy h1{font-weight:400;font-size:76px;line-height:1;color:var(--white)}
  .slider-copy h2{font-weight:400;font-size:40px;line-height:42px;color:var(--red);margin-top:4px}
  .slider-copy p{font-size:13px;line-height:14px;width:300px;margin-left:auto;margin-top:4px}
  .slider-copy .more{display:block;margin-top:22px;font-size:17px}
  .slider-bar{left:0;top:571px;width:1093px;height:56px;background:linear-gradient(#3b3b3b,#1f1f1f)}
  .dots{right:30px;top:16px;display:flex;gap:11px}
  .dots span{width:23px;height:23px;border-radius:50%;background:#fff}
  .dots span.active{background:#000}

  /* search */
  .search{left:54px;top:811px;width:341px;height:610px;background:var(--green);border-radius:5px}
  .search h3{position:absolute;left:29px;top:24px;font-weight:400;font-size:34px}
  .search label{position:absolute;left:32px;font-size:18px}
  .field{position:absolute;left:32px;width:279px;height:39px;background:var(--white);border-radius:2px}
  .field .go{position:absolute;right:3px;top:3px;width:33px;height:33px;background:var(--green-dark)}
  .search-btn{position:absolute;left:32px;top:435px;width:128px;height:56px;background:var(--white);color:#8f8f8f;font-size:18px;display:flex;align-items:center;justify-content:center;letter-spacing:1px}

  /* content */
  .section-title{left:429px;width:718px;height:45px;background:var(--white);color:var(--ink);font-weight:400;font-size:29px;padding-left:8px;line-height:45px}
  .company-text{left:429px;top:878px;width:718px;font-size:16.6px;line-height:26px;text-align:justify;color:#f2f2f2}
  .company-text p{margin-bottom:25px}

  .product{width:340px;height:180px}
  .product .thumb{left:0;top:0;width:107px;height:90px}
  .thumb.green{background:linear-gradient(135deg,#6d6d6d,#8fd0a8 55%,#3e3e3e)}
  .thumb.gauge{background:radial-gradient(circle at 60% 55%,#9aa6ff 0%,#4b56c9 30%,#1b1b1b 65%)}
  .product h4{left:118px;top:0;font-weight:400;font-size:24px;color:var(--white)}
  .product .date{left:118px;top:36px;font-size:16px;color:#777}
  .product p{left:0;top:100px;width:300px;font-size:12.5px;line-height:14.5px;color:#8a8a8a}

  .promo{left:54px;top:1464px;width:341px;height:325px;background:var(--promo);padding:20px 24px}
  .promo .bold{font-weight:700;font-size:54px;line-height:48px}
  .promo .light{font-weight:400;font-size:40px;line-height:48px;margin-top:4px}
  .promo .more{position:absolute;left:220px;top:277px;width:110px;height:35px;background:var(--white);color:#000;font-weight:700;font-size:15px;display:flex;align-items:center;justify-content:center}

  /* footer */
  .footer{left:0;top:1840px;width:1200px;height:336px;background:var(--footer);font-family:var(--sans)}
  .zigzag{left:0;top:-6px}
  .foot-col{top:68px}
  .foot-col h5{font-size:16px;font-weight:700;margin-bottom:14px}
  .foot-col ul{list-style:none}
  .foot-col li{font-size:13.5px;line-height:25px;display:flex;align-items:center;gap:8px;padding-left:10px}
  .foot-col svg{flex:none}
  .contact-title{left:690px;top:58px;font-size:23px;font-weight:700}
  .input{background:var(--white);color:#333;font-size:13px;padding:6px 18px}
  .submit{left:690px;top:283px;width:92px;height:32px;background:linear-gradient(#333,#111);border:1px solid #555;font-size:13px;display:flex;align-items:center;justify-content:center}
  .bottom{left:0;top:2176px;width:1200px;height:62px;background:var(--footer);border-top:2px dashed var(--footer-line);font-family:var(--sans);font-size:13px}
  .bottom .copy{left:112px;top:24px}
  .bottom .social{left:778px;top:24px}
  .social-icons{left:907px;top:18px;display:flex;gap:16px}
  .social-icons span{width:22px;height:22px;border-radius:3px}
</style>
</head>
<body>

<div class="abs topbar">
  <div class="abs links"><span>Home</span><span>Blog</span><span>Contact Us</span><span>Testimonials</span></div>
  <div class="abs register">You have not yet registered <span class="signup">Sign Up</span> Or <span class="login">Log In</span></div>
  <div class="abs call">Call Us At 0100-5550-123</div>
</div>

<header class="abs header">
  <div class="abs brand"><span class="brand-mark"></span><span class="brand-name">Brackwood Tooling</span></div>
  <nav class="abs nav">
    <a>Home</a><a>New CNC Machines</a><a>Used Machines</a><a>Manufacturing</a><a>Contact</a>
  </nav>
</header>

<section class="abs slider">
  <div class="abs slider-photo" role="img" aria-label="Night view of an industrial refinery plant lit with orange lights"></div>
  <svg class="abs slider-overlay" width="1093" height="571" viewBox="0 0 1093 571"><polygon points="490,0 1093,0 1093,464" fill="#1e1e1e" fill-opacity="0.88"/></svg>
  <div class="abs slider-copy">
    <h1>World-class</h1>
    <h2>CNC Conventional<br>Machine Tools</h2>
    <p>Brackwood Tooling is an established vendor of new and used machine tools, with over 30years' experience in buying, rebuild retrofitting and new machine tools We are a global leader in making of new CNC machines , as we make conventional machines into Cheaper CNC machine.</p>
    <span class="more">READ MORE</span>
  </div>
  <div class="abs slider-bar">
    <div class="abs dots"><span></span><span class="active"></span><span></span><span></span><span></span><span></span></div>
  </div>
</section>

<aside class="abs search">
  <h3>Search</h3>
  <label style="top:84px">Title</label>
  <div class="field" style="top:120px"></div>
  <label style="top:175px">Class</label>
  <div class="field" style="top:203px"><span class="go"><svg width="33" height="33" viewBox="0 0 33 33"><circle cx="16.5" cy="16.5" r="11" fill="none" stroke="#fff" stroke-width="2"/><path d="M13 11l7 5.5-7 5.5" fill="none" stroke="#fff" stroke-width="2.4"/></svg></span></div>
  <label style="top:253px">Year Made</label>
  <div class="field" style="top:282px"><span class="go"><svg width="33" height="33" viewBox="0 0 33 33"><circle cx="16.5" cy="16.5" r="11" fill="none" stroke="#fff" stroke-width="2"/><path d="M13 11l7 5.5-7 5.5" fill="none" stroke="#fff" stroke-width="2.4"/></svg></span></div>
  <label style="top:335px">Model</label>
  <div class="field" style="top:363px"><span class="go"><svg width="33" height="33" viewBox="0 0 33 33"><circle cx="16.5" cy="16.5" r="11" fill="none" stroke="#fff" stroke-width="2"/><path d="M13 11l7 5.5-7 5.5" fill="none" stroke="#fff" stroke-width="2.4"/></svg></span></div>
  <div class="search-btn">SEARCH</div>
</aside>

<h2 class="abs section-title" style="top:821px">Our Company</h2>
<div class="abs company-text">
  <p>Brackwood Tooling is an established vendor of new and used machine tools, with over 30 years' experience in buying, rebuilding, retrofitting and commissioning machine tools WORLDWIDE. We have industrial space both in London and Mumbai, where we store over 200 machines at any given time. We specialise in gear manufacturing, pressure diecasting, plano miller, boring and grinding machines, as well as heat treatment facilities, machining and turning centres. Such machines find their usage in the automotive, aviation, power generation, mining and construction industries. Our stock includes the industry's best brands such as Glenmore, Pfalzer, Hurlin and Bohlen. The stock comprises both CNC and conventional machines.</p>
  <p>We are a global leader in the production of new CNC machines, as we retrofit conventional machines into affordable CNC machine tools.</p>
  <p>We also have a gear manufacturing facility in Mumbai, producing quality bespoke gears for some of India's leading Original Equipment Manufacturers. We can produce gears from 16mm to 1600 mm in diameter.</p>
  <p>BRACKWOOD TOOLING</p>
</div>

<h2 class="abs section-title" style="top:1394px">Products.</h2>

<div class="abs product" style="left:429px;top:1464px">
  <div class="abs thumb green" role="img" aria-label="Green CNC vertical turning lathe component"></div>
  <h4 class="abs">CNC Defum VTL.</h4><span class="abs date">13/9/12</span>
  <p class="abs">We are a global leader in the production of new CNC machines, as we retrofit conventional machines into affordable CNC machine tools.</p>
</div>
<div class="abs product" style="left:800px;top:1464px">
  <div class="abs thumb gauge" role="img" aria-label="Close-up of a machine dial gauge"></div>
  <h4 class="abs">CNC Defum VTL</h4>
  <p class="abs">We are a global leader in the production of new CNC machines, as we retrofit conventional machines into affordable CNC machine tools.</p>
</div>
<div class="abs product" style="left:429px;top:1650px">
  <div class="abs thumb green" role="img" aria-label="Green CNC vertical turning lathe component"></div>
  <h4 class="abs">CNC Defum VTL.</h4><span class="abs date">13/9/12</span>
  <p class="abs">We are a global leader in the production of new CNC machines, as we retrofit conventional machines into affordable CNC machine tools.</p>
</div>
<div class="abs product" style="left:800px;top:1650px">
  <div class="abs thumb gauge" role="img" aria-label="Close-up of a machine dial gauge"></div>
  <h4 class="abs">CNC Defum VTL</h4>
  <p class="abs">We are a global leader in the production of new CNC machines, as we retrofit conventional machines into affordable CNC machine tools.</p>
</div>

<div class="abs promo">
  <div class="bold">Different<br>Wholesale</div>
  <div class="light">Products<br>Available at<br>Discount prices</div>
  <span class="more">READ MORE</span>
</div>

<footer class="abs footer">
  <svg class="abs zigzag" width="1200" height="8" viewBox="0 0 1200 8"><pattern id="teeth" width="8" height="8" patternUnits="userSpaceOnUse"><path d="M0 8L4 2L8 8Z" fill="#fff"/></pattern><rect width="1200" height="8" fill="url(#teeth)"/></svg>
  <div class="abs foot-col" style="left:112px">
    <h5>Services</h5>
    <ul>
      <li><svg width="14" height="10" viewBox="0 0 14 10"><path d="M1 5h11M8 1l4 4-4 4" stroke="#fff" stroke-width="1.6" fill="none"/></svg>Vestibulum Ante</li>
      <li><svg width="14" height="10" viewBox="0 0 14 10"><path d="M1 5h11M8 1l4 4-4 4" stroke="#fff" stroke-width="1.6" fill="none"/></svg>Sipsum Primis in Faucibus</li>
      <li><svg width="14" height="10" viewBox="0 0 14 10"><path d="M1 5h11M8 1l4 4-4 4" stroke="#fff" stroke-width="1.6" fill="none"/></svg>Orci Luctus et Ultrices</li>
      <li><svg width="14" height="10" viewBox="0 0 14 10"><path d="M1 5h11M8 1l4 4-4 4" stroke="#fff" stroke-width="1.6" fill="none"/></svg>Posuere&nbsp; at Sed Accusom</li>
      <li><svg width="14" height="10" viewBox="0 0 14 10"><path d="M1 5h11M8 1l4 4-4 4" stroke="#fff" stroke-width="1.6" fill="none"/></svg>Magnus Lorem Quisit</li>
      <li><svg width="14" height="10" viewBox="0 0 14 10"><path d="M1 5h11M8 1l4 4-4 4" stroke="#fff" stroke-width="1.6" fill="none"/></svg>Aenean id Dolroest Pursus</li>
      <li><svg width="14" height="10" viewBox="0 0 14 10"><path d="M1 5h11M8 1l4 4-4 4" stroke="#fff" stroke-width="1.6" fill="none"/></svg>Nulla Quam Mollis</li>
    </ul>
  </div>
  <div class="abs foot-col" style="left:403px">
    <h5>Other Links &amp; Information</h5>
    <ul>
      <li><svg width="14" height="10" viewBox="0 0 14 10"><path d="M1 5h11M8 1l4 4-4 4" stroke="#fff" stroke-width="1.6" fill="none"/></svg>Vestibulum Ante</li>
      <li><svg width="14" height="10" viewBox="0 0 14 10"><path d="M1 5h11M8 1l4 4-4 4" stroke="#fff" stroke-width="1.6" fill="none"/></svg>Sipsum Primis in Faucibus</li>
      <li><svg width="14" height="10" viewBox="0 0 14 10"><path d="M1 5h11M8 1l4 4-4 4" stroke="#fff" stroke-width="1.6" fill="none"/></svg>Orci Luctus et Ultrices</li>
      <li><svg width="14" height="10" viewBox="0 0 14 10"><path d="M1 5h11M8 1l4 4-4 4" stroke="#fff" stroke-width="1.6" fill="none"/></svg>Posuere&nbsp; at Sed Accusom</li>
      <li><svg width="14" height="10" viewBox="0 0 14 10"><path d="M1 5h11M8 1l4 4-4 4" stroke="#fff" stroke-width="1.6" fill="none"/></svg>Magnus Lorem Quisit</li>
      <li><svg width="14" height="10" viewBox="0 0 14 10"><path d="M1 5h11M8 1l4 4-4 4" stroke="#fff" stroke-width="1.6" fill="none"/></svg>Aenean id Dolroest Pursus</li>
      <li><svg width="14" height="10" viewBox="0 0 14 10"><path d="M1 5h11M8 1l4 4-4 4" stroke="#fff" stroke-width="1.6" fill="none"/></svg>Nulla Quam Mollis</li>
    </ul>
  </div>
  <div class="abs contact-title">Questions for Us?</div>
  <div class="abs input" style="left:691px;top:117px;width:184px;height:32px">Subject</div>
  <div class="abs input" style="left:891px;top:117px;width:184px;height:32px">Email</div>
  <div class="abs input" style="left:691px;top:163px;width:384px;height:96px;padding-top:14px">Message</div>
  <div class="abs submit">Submit</div>
</footer>

<div class="abs bottom">
  <span class="abs copy">© All Rights Reserved 2012</span>
  <span class="abs social">Socialize With Us</span>
  <div class="abs social-icons">
    <span style="background:#3aa9d6"></span>
    <span style="background:#2f79b5"></span>
    <span style="background:#555"></span>
    <span style="background:#3b5a98"></span>
    <span style="background:#3c7fb4"></span>
  </div>
</div>

</body>
</html>
```